TLPB Business Card Design

Business card for sole operator professional civil and traffic engineer.
Clients are developers and planners who require assistance with traffic strategic master planning advice and design development for access and infrastructure associated with the development.
Colours already in use are greens for the business name and black for other legend. The attached file shows the letterhead template which is currently in use.
Target Market(s)
Professional Clients in development industry
Most clients known to the Principal and card is mostly required to allow ongoing contact
Industry/Entity Type
Business
Contact Information for Business Card
DESMOND HALVERTON CONSULTING SERVICES
ABN 37 818 502 194
PO Box 871 KERRAWAY NSW 2619
Desmond Halverton 0431 558 906
desmond.halverton@quillmarsh.net

```html
<!DOCTYPE html>
<html lang="en">
<head>
<meta charset="utf-8">
<title>TLPB Business Card</title>
<link href="https://fonts.googleapis.com/css2?family=Cinzel:wght@600;700&family=Open+Sans:wght@400;600&display=swap" rel="stylesheet">
<style>
  :root {
    --backdrop: #c9cacc;
    --card-white: #ffffff;
    --brand-green: #1fa84a;
    --band-green: #2bb24c;
    --rule-grey: #b9bbbd;
    --panel-black: #111214;
    --panel-black-soft: #1e2023;
    --text-white: #f2f2f2;
    --divider: #8a8c8f;
  }
  * { box-sizing: border-box; margin: 0; padding: 0; }
  html, body {
    width: 1200px; height: 900px; overflow: hidden;
    background: var(--backdrop);
  }
  .card {
    position: absolute; left: 150px; top: 192px;
    width: 900px; height: 516px;
    border-radius: 40px; overflow: hidden;
    background: var(--card-white);
    box-shadow: 0 18px 40px rgba(0,0,0,0.18);
  }
  .brand {
    position: absolute; left: 0; top: 0; width: 100%; height: 300px;
    text-align: center;
  }
  .brand-mark {
    position: absolute; left: 0; right: 0; top: 62px;
    font-family: "Cinzel", serif; font-weight: 700;
    font-size: 112px; line-height: 1; letter-spacing: 6px;
    color: var(--brand-green);
  }
  .brand-name {
    position: absolute; left: 0; right: 0; top: 238px;
    font-family: "Cinzel", serif; font-weight: 700;
    font-size: 31px; line-height: 1; letter-spacing: 0.5px;
    color: var(--brand-green);
  }
  .rule-grey {
    position: absolute; left: 0; top: 296px; width: 100%; height: 6px;
    background: linear-gradient(#e3e4e5, var(--rule-grey));
  }
  .band-green {
    position: absolute; left: 0; top: 302px; width: 100%; height: 22px;
    background: var(--band-green);
  }
  .panel {
    position: absolute; left: 0; top: 324px; width: 100%; height: 192px;
    background: radial-gradient(ellipse at 50% 40%, var(--panel-black-soft), var(--panel-black) 75%);
  }
  .person {
    position: absolute; right: 418px; top: 58px; text-align: right;
    font-family: "Open Sans", sans-serif;
  }
  .person-name {
    font-weight: 600; font-size: 31px; line-height: 1.1;
    color: var(--brand-green);
  }
  .person-role {
    font-size: 17px; color: var(--text-white); margin-top: 2px;
  }
  .divider {
    position: absolute; left: 496px; top: 20px; width: 2px; height: 150px;
    background: var(--divider);
  }
  .contacts {
    position: absolute; left: 520px; top: 34px; list-style: none;
    font-family: "Open Sans", sans-serif; font-size: 19px;
    line-height: 24px; color: var(--text-white);
  }
  .contacts li { display: flex; align-items: center; gap: 7px; }
  .contacts .icon { width: 20px; height: 20px; flex: none; fill: var(--band-green); }
  .contacts .no-icon { padding-left: 27px; }
</style>
</head>
<body>
  <div class="card">
    <header class="brand">
      <div class="brand-mark">TLPB</div>
      <div class="brand-name">DESMOND HALVERTON CONSULTING SERVICES</div>
    </header>
    <div class="rule-grey"></div>
    <div class="band-green"></div>
    <section class="panel">
      <div class="person">
        <div class="person-name">Desmond Halverton</div>
        <div class="person-role">Managing Director</div>
      </div>
      <div class="divider"></div>
      <ul class="contacts">
        <li>
          <svg class="icon" viewBox="0 0 24 24" aria-hidden="true"><path d="M6.6 10.8a15.1 15.1 0 0 0 6.6 6.6l2.2-2.2c.3-.3.7-.4 1-.2 1.1.4 2.3.6 3.6.6.6 0 1 .4 1 1V20c0 .6-.4 1-1 1A17 17 0 0 1 3 4c0-.6.4-1 1-1h3.5c.6 0 1 .4 1 1 0 1.3.2 2.5.6 3.6.1.3 0 .7-.2 1z"/></svg>
          0431 558 906
        </li>
        <li>
          <svg class="icon" viewBox="0 0 24 24" aria-hidden="true"><path d="M12 3 2 12h3v8h5v-6h4v6h5v-8h3z"/></svg>
          PO Box 871 KERRAWAY NSW 2619
        </li>
        <li>
          <svg class="icon" viewBox="0 0 24 24" aria-hidden="true"><path d="M3 6h18v12H3z M3 6l9 7 9-7" stroke="#111214" stroke-width="1.5"/></svg>
          desmond.halverton@quillmarsh.net
        </li>
        <li class="no-icon">ABN 37 818 502 194</li>
      </ul>
    </section>
  </div>
</body>
</html>
```